Lumen Haven is a Smart Device and Wiring Business offering the latest in Smart Home Devices inc

Looking for a new website to draw people to my business and explain what a smart home is all about. I currently own a domain and have a website I put together in sitemaxo business website builder. address www.lumenhaven.example. The website needs modernising and be visually appealing with cool action buttons, client feedback page etc.

The webpage needs to present an image of seamless integration of wireless voice control and smart devices that take tasks and activities away from the owner saving them time and money.

I have a chatterbook business page(lumen haven) and snapgrove linked with the business, are we able to link this to the website somehow?

Target Market(s)

Residential home owners who want to modernise their home. Who have seen adverts for orbix nest and kestral vela and want to put it in their home.

Industry/Entity Type

Technology Equipment

Number of Pages Required

1 page

Colors

Designer to choose colors to be used in the design.

Requirements
Must have
• A great landing page, that is modern and attractive, that gets across the idea of smart devices and technology.
• Must be ios/android device friendly.
Nice to have
• interactive/animated buttons
• I like the direction and interactiveness of these websites, a simplified version would be awesome.
• Something in between:
• http://www.casaquilnest.example/ and https://plovex.example/
• http://www.casaquilnest.example/

```html
<!DOCTYPE html>
<html lang="en">
<head>
<meta charset="utf-8">
<title>Lumen Haven — Smart Device Integration</title>
<link href="https://fonts.googleapis.com/css2?family=Montserrat:wght@400;500;600;700&family=Open+Sans:wght@400;600&display=swap" rel="stylesheet">
<style>
  :root{
    --blue:#1a9ad8;
    --blue-light:#1fb4ea;
    --blue-dark:#0b68ad;
    --blue-ring:#0a5c99;
    --ink:#1d2126;
    --grey-text:#6b6f75;
    --ring-grey:#d4d7db;
    --dark-panel:#1f2429;
    --footer:#26292d;
    --white:#ffffff;
  }
  *{margin:0;padding:0;box-sizing:border-box}
  html,body{width:1200px;height:2761px;overflow:hidden;background:var(--white)}
  body{position:relative;font-family:'Montserrat',sans-serif;color:var(--ink)}

  /* Header */
  .site-header{position:absolute;top:0;left:0;width:1200px;height:97px;background:var(--white);border-top:4px solid var(--blue)}
  .brand{position:absolute;left:24px;top:24px;display:flex;align-items:center;gap:12px}
  .brand-dot{width:44px;height:44px;border-radius:50%;background:var(--blue)}
  .brand-name{font-size:26px;font-weight:700;color:var(--ink);letter-spacing:.5px}
  .main-nav{position:absolute;left:305px;top:39px;display:flex;gap:26px;font-size:12px;font-weight:500}
  .main-nav a{color:var(--ink);text-decoration:none}
  .main-nav a.active{color:var(--blue)}
  .header-phone{position:absolute;left:820px;top:30px;display:flex;align-items:center;gap:12px;color:var(--blue);font-size:25px;font-weight:500}
  .quick-contact{position:absolute;left:1050px;top:31px;width:128px;height:40px;background:#15171a;color:var(--white);font-size:12px;font-weight:600;display:flex;align-items:center;justify-content:center}

  /* Hero */
  .hero{position:absolute;top:97px;left:0;width:1200px;height:549px;background:linear-gradient(100deg,#2a2622 0%,#4a3f36 35%,#6a6763 60%,#2f3338 100%)}
  .hero-copy{position:absolute;left:118px;top:137px;color:var(--white);width:420px}
  .eyebrow{font-size:13px;font-weight:700;letter-spacing:.3px}
  .hero-title{margin-top:20px;font-size:44px;font-weight:500;line-height:54px}
  .hero-text{margin-top:14px;font-size:13.5px;line-height:19px;font-family:'Open Sans',sans-serif}
  .btn-blue{display:inline-flex;align-items:center;gap:14px;background:var(--blue);color:var(--white);font-weight:700;font-size:11px}
  .hero .btn-blue{margin-top:30px;height:38px;padding:0 20px}

  /* Integration */
  .integration-title{position:absolute;top:726px;width:1200px;text-align:center;font-size:38px;font-weight:500;color:var(--blue)}
  .integration-sub{position:absolute;top:776px;width:1200px;text-align:center;font-size:14px;line-height:18px;color:var(--grey-text);font-family:'Open Sans',sans-serif}
  .wheel{position:absolute;top:860px;left:0}
  .wheel text{font-family:'Open Sans',sans-serif}

  /* About */
  .about{position:absolute;top:1798px;left:0;width:1200px;height:580px;background:var(--dark-panel)}
  .about-photo{position:absolute;left:0;top:0;width:635px;height:580px;background:linear-gradient(120deg,#8a7f78 0%,#d9dde0 45%,#6c6a66 100%)}
  .about-frame{position:absolute;left:585px;top:157px;width:133px;height:337px;border:1px solid var(--blue);border-right:none}
  .about-copy{position:absolute;left:675px;top:210px;width:400px;color:var(--white)}
  .about-kicker{font-size:20px;font-weight:600;color:#c9ccd0}
  .about-title{margin-top:8px;font-size:40px;font-weight:500;color:var(--blue-light)}
  .about-text{margin-top:12px;font-size:13.5px;line-height:19px;font-family:'Open Sans',sans-serif}
  .about .btn-blue{margin-top:22px;height:26px;padding:0 20px;font-size:10px}

  /* Contact band */
  .contact-band{position:absolute;top:2378px;left:0;width:1200px;height:136px;background:linear-gradient(90deg,#0d8dcf,#1da8e3 50%,#0a84c8)}
  .contact-lead{position:absolute;left:160px;top:36px;width:340px;text-align:center;color:var(--white);font-size:25px;line-height:33px}
  .contact-number{position:absolute;left:538px;top:30px;color:var(--white);font-size:62px;font-weight:400}

  /* Footer */
  .site-footer{position:absolute;top:2514px;left:0;width:1200px;height:247px;background:var(--footer);color:var(--white)}
  .footer-nav{position:absolute;left:118px;top:56px;display:flex;gap:24px;font-size:11px}
  .copyright{position:absolute;left:118px;top:80px;font-size:11px}
  .stay{position:absolute;left:942px;top:56px;font-size:11px}
  .social{position:absolute;left:942px;top:78px;display:flex;gap:6px}
  .social span{width:30px;height:30px;background:var(--white);display:block}
</style>
</head>
<body>

<header class="site-header">
  <div class="brand"><span class="brand-dot"></span><span class="brand-name">Lumen Haven</span></div>
  <nav class="main-nav">
    <a class="active">Home</a><a>What we do</a><a>Products</a><a>About</a><a>Contact</a>
  </nav>
  <div class="header-phone">
    <svg width="24" height="24" viewBox="0 0 24 24"><circle cx="12" cy="12" r="12" fill="var(--blue)"/><rect x="8" y="5" width="8" height="14" rx="1.5" fill="none" stroke="#fff" stroke-width="1.6"/><circle cx="12" cy="16.5" r="0.9" fill="#fff"/></svg>
    0491 570 156
  </div>
  <div class="quick-contact">Quick Contact</div>
</header>

<section class="hero" role="img" aria-label="Photo of a smiling woman with glasses holding a smartphone in front of a laptop">
  <div class="hero-copy">
    <p class="eyebrow">SMART HOME</p>
    <h1 class="hero-title">SMART DEVICE<br>INTEGRATION</h1>
    <p class="hero-text">We are focused on delivering affordable and easily usable devices for your home and office. Wireless smart home - no need for pre-wired cabling</p>
    <span class="btn-blue">LEARN MORE <svg width="8" height="10" viewBox="0 0 8 10"><path d="M2 1l4 4-4 4" stroke="#fff" stroke-width="1.8" fill="none"/></svg></span>
  </div>
</section>

<h2 class="integration-title">SMART DEVICE INTEGRATION</h2>
<p class="integration-sub">how we can help you take full advantage of your smart Assistant<br>and control your home</p>

<svg class="wheel" width="1200" height="820" viewBox="0 0 1200 820">
  <line x1="96" y1="412" x2="1082" y2="412" stroke="var(--blue)" stroke-width="2"/>
  <circle cx="96" cy="412" r="8" fill="var(--blue)"/><circle cx="1082" cy="412" r="8" fill="var(--blue)"/>
  <circle cx="590" cy="412" r="383" fill="var(--ring-grey)"/>
  <g class="segments">
    <path d="M590 47 A365 365 0 0 1 848.1 153.9 L743.4 258.6 A217 217 0 0 0 590 195Z" fill="var(--blue-light)"/>
    <path d="M848.1 153.9 A365 365 0 0 1 955 412 L807 412 A217 217 0 0 0 743.4 258.6Z" fill="var(--blue-dark)"/>
    <path d="M955 412 A365 365 0 0 1 848.1 670.1 L743.4 565.4 A217 217 0 0 0 807 412Z" fill="var(--blue-light)"/>
    <path d="M848.1 670.1 A365 365 0 0 1 590 777 L590 629 A217 217 0 0 0 743.4 565.4Z" fill="var(--blue-dark)"/>
    <path d="M590 777 A365 365 0 0 1 331.9 670.1 L436.6 565.4 A217 217 0 0 0 590 629Z" fill="var(--blue-light)"/>
    <path d="M331.9 670.1 A365 365 0 0 1 225 412 L373 412 A217 217 0 0 0 436.6 565.4Z" fill="var(--blue-dark)"/>
    <path d="M225 412 A365 365 0 0 1 331.9 153.9 L436.6 258.6 A217 217 0 0 0 373 412Z" fill="var(--blue-light)"/>
    <path d="M331.9 153.9 A365 365 0 0 1 590 47 L590 195 A217 217 0 0 0 436.6 258.6Z" fill="var(--blue-dark)"/>
  </g>
  <circle cx="590" cy="412" r="217" fill="var(--blue-ring)"/>
  <g stroke="var(--ring-grey)" stroke-width="6">
    <line x1="590" y1="412" x2="590" y2="29"/><line x1="590" y1="412" x2="860.8" y2="141.2"/>
    <line x1="590" y1="412" x2="973" y2="412"/><line x1="590" y1="412" x2="860.8" y2="682.8"/>
    <line x1="590" y1="412" x2="590" y2="795"/><line x1="590" y1="412" x2="319.2" y2="682.8"/>
    <line x1="590" y1="412" x2="207" y2="412"/><line x1="590" y1="412" x2="319.2" y2="141.2"/>
  </g>
  <g fill="var(--blue)">
    <circle cx="590" cy="29" r="8"/><circle cx="860.8" cy="141.2" r="8"/><circle cx="973" cy="412" r="8"/><circle cx="860.8" cy="682.8" r="8"/>
    <circle cx="590" cy="795" r="8"/><circle cx="319.2" cy="682.8" r="8"/><circle cx="207" cy="412" r="8"/><circle cx="319.2" cy="141.2" r="8"/>
  </g>
  <circle cx="590" cy="412" r="175" fill="var(--white)"/>
  <circle cx="590" cy="362" r="34" fill="var(--blue)"/>
  <text x="590" y="445" text-anchor="middle" font-size="40" font-weight="600" fill="#1d2126" style="font-family:'Montserrat',sans-serif">Lumen Haven</text>

  <g fill="#fff" font-size="22" text-anchor="middle" opacity=".9">
    <text x="665" y="240">01</text><text x="771" y="345">02</text><text x="771" y="495">03</text><text x="665" y="601">04</text>
    <text x="515" y="601">05</text><text x="409" y="495">06</text><text x="409" y="345">07</text><text x="515" y="240">08</text>
  </g>

  <g fill="#fff" font-size="15" text-anchor="middle">
    <text x="704" y="180">Multi-Room Audio</text>
    <text x="868" y="336">Voice Assistant</text>
    <text x="864" y="554">Smart CCTV</text>
    <text x="702" y="716">Smart Blinds</text>
    <text x="474" y="712">Smart Locks</text>
    <text x="322" y="559">Lighting Control</text>
    <text x="305" y="332">Smart Garage</text>
    <text x="481" y="176">Video Doorbell</text>
  </g>

  <g class="icons" fill="#fff" stroke="#fff">
    <!-- audio -->
    <g stroke-width="0"><ellipse cx="686" cy="150" rx="10" ry="8"/><ellipse cx="718" cy="142" rx="10" ry="8"/><rect x="693" y="100" width="4" height="50"/><rect x="725" y="92" width="4" height="50"/><path d="M693 100 L729 92 L729 104 L693 112Z"/></g>
    <!-- mic -->
    <rect x="862" y="252" width="14" height="28" rx="7" stroke-width="0"/><path d="M856 272a13 13 0 0 0 26 0" fill="none" stroke-width="3"/><line x1="869" y1="285" x2="869" y2="300" stroke-width="3"/><line x1="858" y1="300" x2="880" y2="300" stroke-width="3"/>
    <!-- cctv -->
    <rect x="842" y="485" width="44" height="8" stroke-width="0"/><path d="M847 493h34a17 17 0 0 1-34 0Z" stroke-width="0"/><circle cx="864" cy="500" r="6" fill="var(--blue-light)" stroke-width="0"/>
    <!-- power -->
    <path d="M691 653a22 22 0 1 0 22 0" fill="none" stroke-width="5"/><line x1="702" y1="643" x2="702" y2="667" stroke-width="5"/>
    <!-- lock -->
    <path d="M464 660v-10a10 10 0 0 1 20 0v10" fill="none" stroke-width="4"/><rect x="458" y="660" width="32" height="28" rx="2" stroke-width="0"/>
    <!-- bulb -->
    <circle cx="322" cy="508" r="12" stroke-width="0"/><rect x="316" y="518" width="12" height="12" stroke-width="0"/>
    <g stroke-width="3"><line x1="322" y1="484" x2="322" y2="490"/><line x1="300" y1="508" x2="306" y2="508"/><line x1="338" y1="508" x2="344" y2="508"/><line x1="306" y1="492" x2="310" y2="496"/><line x1="338" y1="492" x2="334" y2="496"/></g>
    <!-- wifi -->
    <g fill="none" stroke-width="4"><path d="M287 286a26 26 0 0 1 36 0"/><path d="M294 294a16 16 0 0 1 22 0"/></g><circle cx="305" cy="304" r="4" stroke-width="0"/>
    <!-- doorbell -->
    <rect x="469" y="92" width="24" height="50" rx="2" fill="none" stroke-width="3"/><rect x="474" y="99" width="14" height="4" stroke-width="0"/><circle cx="481" cy="130" r="4" stroke-width="0"/>
    <g stroke-width="0"><rect x="474" y="107" width="4" height="3"/><rect x="484" y="107" width="4" height="3"/><rect x="474" y="113" width="4" height="3"/><rect x="484" y="113" width="4" height="3"/></g>
  </g>
</svg>

<section class="about">
  <div class="about-photo" role="img" aria-label="Photo of a hand holding a smartphone in a bright living room"></div>
  <div class="about-frame"></div>
  <div class="about-copy">
    <p class="about-kicker">ABOUT</p>
    <h2 class="about-title">LUMEN HAVEN</h2>
    <p class="about-text">Lumen Haven began as an idea in a garage and a belief that home technology should be readily available and reasonably priced. We are constantly sourcing and experimenting with new technologies and solutions to create any vision of the future you can imagine.</p>
    <span class="btn-blue">Learn More</span>
  </div>
</section>

<section class="contact-band">
  <p class="contact-lead">Contact us to and out how we can help you</p>
  <p class="contact-number">0491 570 156</p>
</section>

<footer class="site-footer">
  <nav class="footer-nav"><span>Home</span><span>What we do</span><span>Products</span><span>About</span><span>Contact</span></nav>
  <p class="copyright">Allright reserved copyrith © 2018</p>
  <p class="stay">Stay Connected</p>
  <div class="social"><span></span><span></span><span></span><span></span></div>
</footer>

</body>
</html>
```